Banner Ad

We need a banner ad for a service. The service is called, "PipeRook" It compiles tweets and Chatterloom posts about state government issues that are posted by U.S. State Legislators. We have a word cloud containing the issues we want to highlight. And we a logo for PipeRook.

The tag is:
Question: Who Is Talking About Issues on Social Media?
Answer: State Legislators
Are you Listening?

The banner ad will be used for print and web. It will go into a regular weekly publication called The Regional Ledger Roundup. http://www.civicpanel-example.com/the-regional-ledger-roundup/

Industry/Entity Type

Government

```html
<!DOCTYPE html>
<html lang="en">
<head>
<meta charset="utf-8">
<title>PipeRook — Are You Listening?</title>
<link rel="stylesheet" href="https://fonts.googleapis.com/css2?family=Marcellus+SC&family=Roboto+Condensed:wght@400;500&display=swap">
<style>
  :root {
    --teal-deep: #1b5f78;
    --teal-mid: #2f8fa6;
    --cyan-glow: #c9f3f6;
    --mint-glow: #9fe6c4;
    --white: #ffffff;
    --navy: #0e1f33;
    --band: rgba(255, 255, 255, 0.16);
    --panel: rgba(255, 255, 255, 0.38);
    --ring: rgba(255, 255, 255, 0.45);
  }
  * { margin: 0; padding: 0; box-sizing: border-box; }
  html, body { width: 1200px; height: 927px; overflow: hidden; }
  body { font-family: "Roboto Condensed", "Arial Narrow", sans-serif; }

  .banner {
    position: relative;
    width: 1200px;
    height: 927px;
    overflow: hidden;
    background:
      radial-gradient(ellipse 520px 420px at 560px 470px, var(--cyan-glow) 0%, rgba(160,225,235,0.6) 45%, rgba(0,0,0,0) 100%),
      radial-gradient(ellipse 500px 260px at 900px 880px, var(--mint-glow) 0%, rgba(0,0,0,0) 100%),
      linear-gradient(160deg, var(--teal-deep) 0%, var(--teal-mid) 45%, #3d9ab4 70%, var(--teal-deep) 100%);
  }

  .tag-band {
    position: absolute;
    left: 0; width: 1200px;
    text-align: center;
    font-family: "Marcellus SC", serif;
    color: var(--white);
    letter-spacing: 2px;
  }
  .tag-band--label { background: linear-gradient(90deg, rgba(255,255,255,0) 10%, var(--band) 35%, var(--band) 65%, rgba(255,255,255,0) 90%); }
  .tag-question-label { top: 16px; height: 42px; line-height: 42px; font-size: 26px; }
  .tag-question { top: 60px; font-size: 30px; word-spacing: 8px; }
  .tag-answer-label { top: 115px; height: 40px; line-height: 40px; font-size: 26px; }
  .tag-answer { top: 160px; font-size: 28px; word-spacing: 8px; }

  .map-area {
    position: absolute;
    left: 300px; top: 215px;
    width: 590px; height: 450px;
    border-radius: 45% 40% 42% 38%;
    background: radial-gradient(ellipse at 50% 50%, #3fb7c8 0%, #2a93ad 55%, rgba(40,140,170,0) 100%);
    opacity: 0.85;
  }
  .ring {
    position: absolute;
    left: 350px; top: 207px;
    width: 496px; height: 496px;
  }

  .issue {
    position: absolute;
    line-height: 1;
    white-space: nowrap;
    font-weight: 500;
  }
  .issue--light { color: var(--white); }
  .issue--dark { color: var(--navy); }
  .cloud-left .issue { left: 18px; }
  .cloud-right .issue { right: 18px; }

  .call-out {
    position: absolute;
    top: 725px; left: 0; width: 1200px;
    text-align: center;
    font-family: "Marcellus SC", serif;
    font-size: 28px;
    letter-spacing: 2px;
    word-spacing: 6px;
    color: var(--navy);
  }

  .brand {
    position: absolute;
    left: 22px; top: 800px;
    display: flex; align-items: center; gap: 22px;
  }
  .brand-dot {
    width: 110px; height: 110px; border-radius: 50%;
    background: #8c2a33;
    opacity: 0.85;
  }
  .brand-name {
    font-family: "Marcellus SC", serif;
    font-size: 66px;
    color: var(--navy);
  }

  .social-panel {
    position: absolute;
    left: 725px; top: 785px;
    width: 470px; height: 122px;
    background: var(--panel);
    padding: 12px 14px 0 0;
  }
  .social-line {
    display: flex; align-items: center; justify-content: flex-end; gap: 10px;
    height: 50px;
    font-family: "Marcellus SC", serif;
    font-size: 36px;
    color: var(--navy);
    letter-spacing: 1px;
  }
  .social-dot {
    width: 40px; height: 40px; border-radius: 50%;
    background: rgba(120, 140, 130, 0.75);
  }
</style>
</head>
<body>
<main class="banner">
  <div class="tag-band tag-band--label tag-question-label">Question</div>
  <div class="tag-band tag-question">Who Is Talking About Issues on Social Media?</div>
  <div class="tag-band tag-band--label tag-answer-label">Answer</div>
  <div class="tag-band tag-answer">State Legislators!</div>

  <div class="map-area" role="img" aria-label="Map of the United States with each state shaded in varying teal and aqua tones"></div>
  <svg class="ring" viewBox="0 0 496 496" aria-hidden="true">
    <circle cx="248" cy="248" r="242" fill="none" stroke="var(--ring)" stroke-width="7"/>
  </svg>

  <section class="cloud-left" aria-label="Issues">
    <span class="issue issue--light" style="top:252px;font-size:40px">GMO</span>
    <span class="issue issue--dark" style="top:293px;font-size:58px">CommonCore</span>
    <span class="issue issue--light" style="top:362px;font-size:58px">Fracking</span>
    <span class="issue issue--dark" style="top:430px;font-size:21px">Privacy</span>
    <span class="issue issue--light" style="top:474px;font-size:21px">Bankruptcy</span>
    <span class="issue issue--dark" style="top:518px;font-size:33px">E-Cigs</span>
    <span class="issue issue--light" style="top:564px;font-size:27px">TaxReform</span>
    <span class="issue issue--dark" style="top:598px;font-size:72px">Transportation</span>
  </section>

  <section class="cloud-right" aria-label="More issues">
    <span class="issue issue--light" style="top:240px;font-size:74px">MinimumWage</span>
    <span class="issue issue--dark" style="top:328px;font-size:33px">AlternativeEnergy</span>
    <span class="issue issue--light" style="top:371px;font-size:27px">Drones</span>
    <span class="issue issue--dark" style="top:416px;font-size:40px">SharingEconomy</span>
    <span class="issue issue--light" style="top:484px;font-size:21px">FairShare</span>
    <span class="issue issue--dark" style="top:517px;font-size:56px">ClimateChange</span>
    <span class="issue issue--light" style="top:584px;font-size:45px">Immigration</span>
    <span class="issue issue--dark" style="top:644px;font-size:25px">DistractedDriving</span>
  </section>

  <div class="call-out">Are you Listening?</div>

  <div class="brand">
    <span class="brand-dot" aria-hidden="true"></span>
    <span class="brand-name">PipeRook</span>
  </div>

  <aside class="social-panel">
    <div class="social-line"><span class="social-dot" aria-hidden="true"></span>/CivicPanelGroup</div>
    <div class="social-line"><span class="social-dot" aria-hidden="true"></span>@CivicPanel</div>
  </aside>
</main>
</body>
</html>
```